Brill Insurance Agency - Business Cards

Hello, I am needing new trendy business cards for our Insurance Agency now that I have a new Logo. I have attached our new logo with several color options along with a business card design that I like. I am leaning towards burgundy and blue colors. I have attached our current business card. I have also attached a headshot of our company president, Martin Vale, that you can use if you wish. Thank you so much in advance for all the wonderful designs!!!!

Target Market(s)

We want to look very professional to potential customers and we also want to look very professional so insurance companies will want to contract with us to sell their product.

Industry/Entity Type

Insurance

Contact Information for Business Card

Martin Vale
mvale@brillagency.com
Business: 555-213-4087
Fax: 555-213-7751
Cell: 555-390-2618
Toll Free: 888-555-0194
42 W Elm Rd Butler, MO 64730
www.brillagency.net

Font styles to use
Serif
Sans Serif

Colors
0355a3
3277b5
f04a50
ec1f27

Requirements
Nice to have
• I love creativity. The more creative and balanced a business card design the more I will like it. I would like the card to be printed horizontally instead of vertically.
Should not have
• My project should not have the Allied Coverage Network logo. It is no longer used in the industry.

```html
<!DOCTYPE html>
<html lang="en">
<head>
<meta charset="utf-8">
<title>Brill Insurance Agency – Business Cards</title>
<link href="https://fonts.googleapis.com/css2?family=Mulish:wght@400;500;600;800&display=swap" rel="stylesheet">
<style>
  :root {
    --backdrop: #dcdde0;
    --burgundy: #521426;
    --slate: #4d4d4f;
    --white: #ffffff;
  }
  * { box-sizing: border-box; margin: 0; padding: 0; }
  html, body {
    width: 1047px; height: 1200px; overflow: hidden;
    background: var(--backdrop);
    font-family: "Mulish", sans-serif;
    color: var(--white);
  }
  .card {
    position: absolute; left: 157px; width: 734px; height: 418px;
    box-shadow: 0 2px 10px rgba(0,0,0,0.12);
    overflow: hidden;
  }
  .card-front { top: 157px; background: var(--burgundy); }
  .card-back { top: 626px; background: var(--slate); }

  .front-brand {
    position: absolute; left: 77px; top: 150px; height: 126px;
    display: flex; align-items: center; gap: 31px;
  }
  .brand-dot {
    width: 126px; height: 126px; border-radius: 50%;
    border: 8px solid var(--white); flex: none;
  }
  .brand-name {
    font-weight: 800; font-size: 33px; line-height: 1.12;
    letter-spacing: 0.5px; text-transform: uppercase; white-space: nowrap;
  }
  .web-strip {
    position: absolute; right: 0; top: 0; width: 74px; height: 100%;
    background: var(--slate);
  }
  .web-address {
    position: absolute; left: 50%; top: 50%;
    transform: translate(-50%, -50%) rotate(-90deg);
    white-space: nowrap;
    font-weight: 800; font-size: 20px; letter-spacing: 1.5px;
  }
  .web-address .lower { font-size: 17px; }

  .accent-strip {
    position: absolute; left: 0; top: 0; width: 74px; height: 100%;
    background: var(--burgundy);
  }
  .back-brand {
    position: absolute; right: 28px; top: 28px;
    width: 126px; height: 126px; border-radius: 50%;
    border: 8px solid var(--white);
  }
  .person {
    position: absolute; right: 28px; top: 178px; text-align: right;
  }
  .person-name {
    font-weight: 800; font-size: 30px; letter-spacing: 0.3px;
    text-transform: uppercase;
  }
  .person-title {
    font-weight: 500; font-size: 19px; margin-top: 2px; letter-spacing: 0.3px;
  }
  .contact-list { list-style: none; position: absolute; left: 0; top: 273px; }
  .contact-item {
    height: 31.3px; display: flex; align-items: center;
  }
  .contact-icon {
    width: 74px; display: flex; justify-content: center;
  }
  .contact-icon svg { width: 20px; height: 20px; fill: var(--white); }
  .contact-text {
    padding-left: 14px; font-weight: 500; font-size: 20px; letter-spacing: 0.6px;
    white-space: nowrap;
  }
</style>
</head>
<body>
  <section class="card card-front">
    <div class="front-brand">
      <div class="brand-dot"></div>
      <div class="brand-name">Brill Insurance<br>Agency Inc</div>
    </div>
    <div class="web-strip">
      <div class="web-address">www.BRILLAGENCY<span class="lower">.NET</span></div>
    </div>
  </section>

  <section class="card card-back">
    <div class="accent-strip"></div>
    <div class="back-brand"></div>
    <div class="person">
      <div class="person-name">Martin Vale</div>
      <div class="person-title">OWNER &amp; AGENT</div>
    </div>
    <ul class="contact-list">
      <li class="contact-item">
        <span class="contact-icon"><svg viewBox="0 0 20 20"><path d="M1 4h18v2l-9 6-9-6z"/><path d="M1 8l9 6 9-6v8H1z"/></svg></span>
        <span class="contact-text">mvale@brillagency.com</span>
      </li>
      <li class="contact-item">
        <span class="contact-icon"><svg viewBox="0 0 20 20"><path d="M4 1l3.5 0.5 1 4.5-2.5 1.5c1 2.5 3 4.5 5.5 5.5l1.5-2.5 4.5 1 0.5 3.5c0 1.5-1.5 2.5-3 2.5C8 17 3 12 1.5 4.5 1.5 3 2.5 1 4 1z"/></svg></span>
        <span class="contact-text">555-213-4087</span>
      </li>
      <li class="contact-item">
        <span class="contact-icon"><svg viewBox="0 0 20 20"><path d="M5 1h10v5H5z"/><path d="M2 7h16v8h-3v-3H5v3H2z"/><path d="M6 13h8v6H6z"/></svg></span>
        <span class="contact-text">555-213-7751</span>
      </li>
      <li class="contact-item">
        <span class="contact-icon"><svg viewBox="0 0 20 20"><path d="M10 0a7 7 0 0 0-7 7c0 5 7 13 7 13s7-8 7-13a7 7 0 0 0-7-7zm0 10a3 3 0 1 1 0-6 3 3 0 0 1 0 6z"/></svg></span>
        <span class="contact-text">42 W Elm Rd. Alder Falls, KS 66990</span>
      </li>
    </ul>
  </section>
</body>
</html>
```